Love-Drama Movie Flyer for World Sales Pitch

Dear Designers

We need for a world sales pitch a flyer for our new movie MARBLEFIN. We need a front and a back page A4.
Front: One picture we deliver for then whole page, title, some "pitch" sentences
Picture Front: https://www.fileharbor-example.net/s/qk83tnb2px71vd9/Front_Picture.jpg?dl=0
Back: Arrangement of title, 5 pictures and text we deliver (attached)

Please find in the attached examples a rough idea what we’re looking for. Should not be exactly the same.

To get an Impression of the content and style of the film, please watch the 3min teaser. This will be very important for the style of the flyer:
https://clipvault-example.net/487316920
pw: tutumarblefin

In the end we prefer a data package with the flyer made in a adobe design application for high quality print.

Thanks
Tomas Vrelnik
Producer

Target Market(s)

High profile film sales professionals

Industry/Entity Type

Film Production

Requirements
Must have
• see description
Should not have
• not too generic,
• there is the color red on the actors pullover but red is not really a color in the film. So please don't use much red
• Awards of the actor/actress are not for this movie, it's from other movies

```html
<!DOCTYPE html>
<html lang="en">
<head>
<meta charset="utf-8">
<title>MARBLEFIN – Poster</title>
<link rel="stylesheet" href="https://fonts.googleapis.com/css2?family=Open+Sans:ital,wght@0,300;0,400;1,300&display=swap">
<style>
  :root {
    --backdrop: #0b0b0c;
    --poster-bg: #0e0e0f;
    --poster-edge: #2a2a2c;
    --figure-core: #3a3a3d;
    --figure-mid: #26262a;
    --ink: #f4f4f4;
    --ink-soft: #dcdcdc;
    --ink-muted: #c2c2c2;
  }
  html, body {
    margin: 0;
    padding: 0;
    width: 1200px;
    height: 1200px;
    overflow: hidden;
    background: var(--backdrop);
    font-family: "Open Sans", "Segoe UI", sans-serif;
  }
  .poster {
    position: absolute;
    left: 146px;
    top: 0;
    width: 908px;
    height: 1200px;
    background: radial-gradient(ellipse 55% 50% at 50% 42%, #1a1a1c 0%, var(--poster-bg) 75%);
    border: 1px solid var(--poster-edge);
    box-sizing: border-box;
    color: var(--ink);
  }
  .hero-photo {
    position: absolute;
    left: 297px;
    top: 84px;
    width: 288px;
    height: 980px;
  }
  .title {
    position: absolute;
    left: 0;
    right: 0;
    top: 380px;
    margin: 0;
    text-align: center;
    font-weight: 300;
    font-size: 128px;
    line-height: 1;
  }
  .tagline, .credit {
    position: absolute;
    left: 0;
    right: 0;
    margin: 0;
    text-align: center;
    font-weight: 300;
    font-size: 28px;
    line-height: 1;
    color: var(--ink-soft);
  }
  .tagline { top: 520px; }
  .credit { top: 572px; }
  .cast {
    position: absolute;
    font-weight: 300;
    color: var(--ink-soft);
  }
  .cast--lead { left: 56px; top: 756px; width: 340px; }
  .cast--costar { left: 596px; top: 764px; width: 300px; }
  .cast__name {
    margin: 0;
    font-size: 26px;
    font-weight: 300;
    color: var(--ink);
    line-height: 1.1;
  }
  .cast__role {
    margin: 0 0 12px;
    font-size: 19px;
    font-style: italic;
    font-weight: 300;
  }
  .cast__awards {
    list-style: none;
    margin: 0;
    padding: 0 0 0 2px;
  }
  .cast__awards li {
    font-size: 15px;
    line-height: 18px;
    margin-bottom: 17px;
    text-transform: uppercase;
  }
  .cast__note {
    margin: -8px 0 0 2px;
    font-size: 12px;
    line-height: 1.25;
    color: var(--ink-muted);
    width: 240px;
  }
  .release {
    position: absolute;
    left: 0; right: 0;
    top: 1091px;
    margin: 0;
    text-align: center;
    font-weight: 300;
    font-size: 28px;
    line-height: 1;
  }
  .website {
    position: absolute;
    left: 0; right: 0;
    top: 1133px;
    margin: 0;
    text-align: center;
    font-weight: 300;
    font-size: 26px;
    line-height: 1;
    letter-spacing: 12px;
    padding-left: 12px;
    color: var(--ink-soft);
  }
</style>
</head>
<body>
  <main class="poster">
    <svg class="hero-photo" viewBox="0 0 288 980" preserveAspectRatio="none" role="img" aria-label="Photograph of the lead actor standing front-on in a dark grey hooded sweatshirt, dark jeans and blue sneakers, lit against a black background">
      <defs>
        <radialGradient id="figure-tone" cx="50%" cy="38%" r="62%">
          <stop offset="0%" stop-color="var(--figure-core)"/>
          <stop offset="60%" stop-color="var(--figure-mid)"/>
          <stop offset="100%" stop-color="#141416"/>
        </radialGradient>
      </defs>
      <rect width="288" height="980" rx="40" fill="url(#figure-tone)"/>
    </svg>

    <h1 class="title">MARBLEFIN</h1>
    <p class="tagline">This is David</p>
    <p class="credit">a film by Lukas Brennwald</p>

    <section class="cast cast--lead">
      <h2 class="cast__name">MATTEO KESSLING</h2>
      <p class="cast__role">(name of the actor)</p>
      <ul class="cast__awards">
        <li>Alpine Screen Award 2015<br>Best Actor(for The Lantern)</li>
        <li>European Rising Face 2015</li>
        <li>Recurring appearance in the award winning<br>US series Nightwatch</li>
      </ul>
      <p class="cast__note">Awards of the actor/actress are not for this movie, it's from other movies</p>
    </section>

    <section class="cast cast--costar">
      <h2 class="cast__name">LINA SOPHIE AMREIN</h2>
      <p class="cast__role">(name of the actor)</p>
      <ul class="cast__awards">
        <li>Orbit Award Nominee 2016<br>Best Actress(for North of June)</li>
        <li>Isar Film Award 2015<br>Best Young Actress(for North of June)</li>
        <li>Fresh Talent Award 2012<br>Best Actress(for Margit)</li>
      </ul>
      <p class="cast__note">Awards of the actor/actress are not for this movie, it's from other movies</p>
    </section>

    <p class="release">COMING FALL 2016</p>
    <p class="website">www.lumenfold-films.ch</p>
  </main>
</body>
</html>
```